Harbinger Slabworks, Inc. Business Card

Create a business card that is eye catching and based around concrete sawcutting. I've attached our current business card and logo for reference. We like aspects of the current business card, but it is starting to feel very loud and lost. We would like something that is still fun but is more modern and streamlined.

```html
<!DOCTYPE html>
<html lang="en">
<head>
<meta charset="utf-8">
<title>Harbinger Slabworks, Inc. Business Card</title>
<link rel="stylesheet" href="https://fonts.googleapis.com/css2?family=Open+Sans:wght@400;600;700&display=swap">
<style>
  :root {
    --backdrop: #222222;
    --navy: #1c2458;
    --navy-deep: #161d4a;
    --eagle-blue: #2f56b8;
    --red: #e8202a;
    --yellow: #f7c600;
    --white: #ffffff;
  }
  * { box-sizing: border-box; margin: 0; padding: 0; }
  html, body { width: 1200px; height: 780px; overflow: hidden; }
  body {
    background: var(--backdrop);
    font-family: "Open Sans", Arial, sans-serif;
    color: var(--white);
    position: relative;
  }
  .card {
    position: absolute;
    top: 241px;
    width: 520px;
    height: 297px;
    background: var(--navy);
    box-shadow: 0 18px 40px rgba(0,0,0,0.55);
    overflow: hidden;
  }
  .card--front { left: 60px; }
  .card--back { left: 620px; }

  .brand {
    display: flex;
    align-items: center;
    gap: 8px;
    font-size: 12px;
    font-weight: 600;
    color: var(--white);
  }
  .brand__dot {
    width: 22px; height: 22px;
    border-radius: 50%;
    background: var(--red);
    flex: none;
  }
  .card--front .brand { position: absolute; left: 26px; top: 24px; }

  .holder {
    position: absolute; left: 26px; top: 62px;
    font-size: 24px; font-weight: 700; letter-spacing: 0.5px;
    text-transform: uppercase; line-height: 1;
  }
  .holder__first { color: var(--red); }
  .holder__last { color: var(--yellow); }

  .address {
    position: absolute; left: 26px; top: 96px;
    font-size: 11.5px; line-height: 1.45;
  }
  .contacts {
    position: absolute; left: 26px; bottom: 24px;
    list-style: none; font-size: 11.5px; line-height: 1.55;
  }
  .contacts li { display: flex; align-items: center; gap: 8px; }
  .contacts svg { width: 11px; height: 11px; flex: none; }

  .services {
    position: absolute; right: 26px; top: 26px;
    text-align: right; list-style: none;
    font-size: 12px; line-height: 1.45; text-transform: uppercase;
  }
  .services__title { color: var(--red); font-weight: 700; font-size: 13px; }
  .services li { display: flex; align-items: center; justify-content: flex-end; gap: 7px; }
  .services li::after {
    content: ""; width: 7px; height: 7px; border-radius: 50%; background: var(--red);
  }
  .services li:nth-child(odd)::after { background: var(--yellow); }

  .eagle-art {
    position: absolute; right: 26px; bottom: 20px;
    width: 210px; height: 150px;
    border-radius: 50% 45% 40% 50%;
    background: radial-gradient(ellipse at 45% 40%, var(--eagle-blue), var(--navy) 72%);
  }

  .pattern-field {
    position: absolute; inset: 0;
    background: radial-gradient(ellipse at 20% 80%, #2a3b95, var(--navy-deep) 75%);
  }
  .card--back .brand { position: absolute; right: 30px; bottom: 26px; }
</style>
</head>
<body>
  <section class="card card--front" aria-label="Card front">
    <div class="brand"><span class="brand__dot"></span>Harbinger Slabworks, Inc.</div>
    <h1 class="holder"><span class="holder__first">Marisa</span> <span class="holder__last">Delgado</span></h1>
    <p class="address">218 N. Calder Ave.<br>Westbrook, NJ 07490</p>
    <ul class="contacts">
      <li><svg viewBox="0 0 12 12"><path d="M3 1l2 2-1 2 3 3 2-1 2 2-2 2C5 11 1 7 1 3z" fill="var(--red)"/></svg>855.410.3726 (Office)</li>
      <li><svg viewBox="0 0 12 12"><rect x="3" y="1" width="6" height="10" rx="1" fill="none" stroke="var(--yellow)" stroke-width="1.3"/></svg>973.508.6194 (Cell)</li>
      <li><svg viewBox="0 0 12 12"><circle cx="6" cy="6" r="5" fill="var(--red)"/></svg>www.HarbingerSlabworks.com</li>
      <li><svg viewBox="0 0 12 12"><rect x="1" y="3" width="10" height="7" fill="var(--yellow)"/><path d="M1 3l5 4 5-4" fill="none" stroke="var(--navy)" stroke-width="1"/></svg>Marisa@HarbingerSlabworks.com</li>
    </ul>
    <ul class="services">
      <li class="services__title" style="justify-content:flex-end">Our Services</li>
      <li>Wall Sawing</li>
      <li>Core Drilling</li>
      <li>Slab Sawing</li>
      <li>Breaking &amp; Removal</li>
    </ul>
    <div class="eagle-art" role="img" aria-label="Large embossed eagle head illustration in glossy blue"></div>
  </section>

  <section class="card card--back" aria-label="Card back">
    <div class="pattern-field" role="img" aria-label="Repeating pattern of small embossed eagle heads in blue"></div>
    <div class="brand"><span class="brand__dot"></span>Harbinger Slabworks, Inc.</div>
  </section>
</body>
</html>
```